Web Design Project

We are looking for a new site design for the VELTO Canada. The current site can be found at
http://www.veltocanada-example.org/
The URL is provided for reference. We want a completely different look and layout which is shown in the specifications document.
As part of the design, we want a home page, and inside page.
The design you provide will be implemented in Joomla. The design winner will only need to provide the PSD. We anticipate creating the template coding in-house.
However, if you have experience creating Joomla templates, please let us know as we may ask you to bid separately to do that phase of the project.
We've provided a specifications document which includes wireframes of the home page, and inside page. We've also included a logo file.
For the header at the top, as indicated in the specs document, we want to keep the same overall treatment to every page. We want a graphic treatment with the logo for the header area. In this manner, the design will be flexiable and can be used for future years.
For the home page, we've indicated that we'd like to have a slider implemented within the design.
The wireframe is provided to illustrate the placement of content and menu items. The exact dimensions of each component can be revised as you see fit. We are also flexiable if you feel we have missed items.

```html
<!DOCTYPE html>
<html lang="en">
<head>
<meta charset="utf-8">
<title>VELTO Canada Region</title>
<link href="https://fonts.googleapis.com/css2?family=Roboto+Condensed:wght@400;700&family=Arimo:wght@400;700&display=swap" rel="stylesheet">
<style>
:root{
  --navy:#2f4a8a;
  --blue-top:#2d72be;
  --blue-bot:#1a4f93;
  --blue-active:#1c4585;
  --red-top:#c3161c;
  --red-bot:#960d11;
  --panel:#f2eff0;
  --panel-border:#d9d6d7;
  --text:#2b2b2b;
  --head:#2a2a2a;
  --link-red:#c4121a;
  --link-blue:#2f4a8a;
  --white:#ffffff;
}
*{box-sizing:border-box;margin:0;padding:0}
html,body{width:1200px;height:768px;overflow:hidden}
body{position:relative;font-family:"Arimo",Arial,sans-serif;color:var(--text);
  background:linear-gradient(180deg,#e9f0f7 0%,#cfdde9 30%,#e4ecf3 60%,#f5f7fa 78%,#ffffff 100%)}
.abs{position:absolute}
.backdrop{left:0;top:0;width:1200px;height:689px;
  background:linear-gradient(100deg,rgba(190,210,228,.6) 0%,rgba(240,245,250,.2) 40%,rgba(170,195,220,.55) 100%)}
.top-rule{left:0;top:0;width:1200px;height:7px;background:var(--navy)}
.util-nav{left:802px;top:0;width:276px;height:33px;background:var(--navy);
  clip-path:polygon(0 0,100% 0,98% 100%,3% 100%);border-radius:0 0 6px 6px;
  display:flex;align-items:center;justify-content:center;font:700 12px "Roboto Condensed",sans-serif;color:var(--white)}
.util-nav span{padding:0 9px;border-left:1px solid rgba(255,255,255,.35)}
.util-nav span:first-child{border-left:0}
.brand{left:128px;top:14px;width:100px;height:74px;display:flex;align-items:center;gap:6px}
.brand .dot{width:26px;height:26px;border-radius:50%;background:var(--navy)}
.brand .name{font:700 22px "Roboto Condensed",sans-serif;color:var(--navy)}
.search{left:831px;top:51px;width:247px;height:30px;border-radius:6px;background:#e3e3e3;
  box-shadow:inset 0 1px 3px rgba(0,0,0,.25),0 1px 0 #fff}
.search svg{position:absolute;right:7px;top:7px}
.main-nav{left:120px;top:95px;width:960px;height:36px;display:flex;
  background:linear-gradient(180deg,var(--blue-top),var(--blue-bot))}
.main-nav a{color:var(--white);text-decoration:none;font:700 14px "Roboto Condensed",sans-serif;
  display:flex;align-items:center;justify-content:center;border-left:1px solid rgba(255,255,255,.15)}
.main-nav a:first-child{border-left:0}
.main-nav a.active{background:var(--blue-active)}
.slider{left:120px;top:131px;width:960px;height:151px;background:var(--white);padding:6px 5px 5px;box-shadow:0 1px 4px rgba(0,0,0,.2)}
.slide{position:relative;width:950px;height:140px;
  background:linear-gradient(90deg,#6a4310 0%,#b58a3d 12%,#e1c46a 35%,#e8d27a 55%,#c9a955 70%,#6b4a18 85%,#3b2608 100%)}
.slide h2{position:absolute;left:84px;top:54px;font:700 35px "Roboto Condensed",sans-serif;color:var(--white);
  text-shadow:1px 2px 3px rgba(0,0,0,.45);letter-spacing:-.3px}
.dots{position:absolute;left:21px;top:117px;display:flex;gap:6px}
.dots i{width:12px;height:12px;background:#fff;border:2px solid #ddd;display:block}
.dots i.on{border:2px solid #fff;background:var(--navy)}
.sidebar{left:119px;top:287px;width:240px;height:389px;background:var(--panel);border:1px solid var(--panel-border)}
.bar{position:absolute;left:124px;width:230px;height:35px;background:linear-gradient(180deg,var(--blue-top),var(--blue-bot));
  color:var(--white);font:700 18px "Roboto Condensed",sans-serif;display:flex;align-items:center;padding-left:54px}
.bar .ico{position:absolute;left:12px;top:5px;width:26px;height:25px;border-radius:4px;background:#9fb3c9}
.cta{position:absolute;left:119px;width:240px;height:28px;background:linear-gradient(180deg,var(--red-top),var(--red-bot));
  color:var(--white);font:700 14px "Roboto Condensed",sans-serif;display:flex;align-items:center;justify-content:center;gap:10px;letter-spacing:.3px}
.cta .ico{width:22px;height:16px;background:#e9e2d5;border-radius:2px;margin-right:12px}
.sponsor-row{left:124px;top:335px;width:230px;height:38px;display:flex;align-items:center;justify-content:space-around}
.sponsor-row span{display:block;background:#8c8c8c}
.field{position:absolute;left:134px;width:210px;height:25px;background:#fff;border:1px solid #e0dcdc;
  box-shadow:inset 0 1px 2px rgba(0,0,0,.12);font-size:13px;color:#555;padding:5px 8px}
.btn-login{left:277px;top:524px;width:66px;height:25px;background:linear-gradient(180deg,var(--blue-top),var(--blue-bot));
  color:#fff;font:700 14px "Roboto Condensed",sans-serif;display:flex;align-items:center;justify-content:center}
.social{left:161px;top:633px;display:flex;gap:7px}
.social i{width:25px;height:25px;border-radius:50%;display:block}
.panel{background:var(--panel);border:1px solid var(--panel-border);overflow:hidden}
.panel h3{font:700 20px "Roboto Condensed",sans-serif;color:var(--head);letter-spacing:.3px}
.welcome{left:379px;top:287px;width:440px;height:210px;padding:3px 10px 0 8px}
.welcome h3{border-bottom:1px solid #d0cccd;padding-bottom:5px}
.welcome p{font-size:11.6px;line-height:18px;text-align:justify;margin-top:8px;letter-spacing:-.1px;hyphens:manual}
.welcome p.lead{font-weight:700;margin-top:7px;margin-bottom:18px}
.news{left:829px;top:287px;width:250px;height:210px}
.news h3{height:35px;padding:4px 9px 0;border-bottom:1px solid #d0cccd}
.news-item{position:relative;padding:0 6px;height:87px;border-bottom:1px solid #d0cccd}
.news-item:last-child{border-bottom:0}
.news-item .title{position:absolute;left:6px;top:7px;font:700 12px "Arimo",sans-serif;color:var(--link-red);white-space:nowrap}
.news-item .date{position:absolute;right:3px;top:0;width:104px;height:26px;background:var(--navy);color:#fff;
  font:700 12.5px "Arimo",sans-serif;display:flex;align-items:center;justify-content:center}
.news-item p{position:absolute;left:6px;right:8px;top:31px;font-size:12px;line-height:15px;color:#333}
.news-item .more{position:absolute;left:6px;top:66px;font:700 12px "Arimo",sans-serif;color:var(--link-blue)}
.regions{left:379px;top:503px;width:700px;height:174px}
.regions h3{padding:6px 8px 5px;border-bottom:1px solid #d0cccd}
.region-cols{display:flex;padding:12px 0 0 22px}
.region-cols div{flex:0 0 173px}
.region-cols h4{font:700 14px "Roboto Condensed",sans-serif;color:var(--head);margin-bottom:4px}
.region-cols li{list-style:none;font-size:12.5px;line-height:24px;height:24px;color:#333}
.region-cols li::before{content:"\203A";color:var(--navy);font-weight:700;font-size:16px;line-height:12px;margin-right:6px}
.footer{left:0;top:689px;width:1200px;height:79px;background:var(--navy);color:#fff}
.footer-nav{position:absolute;left:120px;top:9px;width:960px;display:flex;justify-content:space-between;font-size:12.5px;padding:0 7px 0 11px}
.footer-nav span.sep{opacity:.9}
.footer-rule{position:absolute;left:120px;top:37px;width:960px;height:1px;background:rgba(255,255,255,.18)}
.copyright{position:absolute;left:126px;top:51px;font-size:12px}
.privacy{position:absolute;left:995px;top:53px;font-size:12px}
</style>
</head>
<body>
<div class="abs backdrop" role="img" aria-label="Soft sky and glass office tower backdrop"></div>
<div class="abs top-rule"></div>

<nav class="abs util-nav"><span>HOME</span><span>CONTACT US</span><span>VELTO INTERNATIONAL</span></nav>

<div class="abs brand"><span class="dot"></span><span class="name">VELTO</span></div>

<div class="abs search">
  <svg width="18" height="16" viewBox="0 0 18 16"><circle cx="7" cy="6.5" r="4.8" fill="none" stroke="#777" stroke-width="2"/><line x1="10.5" y1="10" x2="16" y2="14.5" stroke="#777" stroke-width="2.6" stroke-linecap="round"/></svg>
</div>

<nav class="abs main-nav">
  <a class="active" style="width:95px">ABOUT</a>
  <a style="width:111px">BOARD</a>
  <a style="width:126px">CHAPTERS</a>
  <a style="width:158px">MEMBER SPACE</a>
  <a style="width:220px">RESOURCES &amp; KNOWLEDGE</a>
  <a style="width:142px">SPONSORSHIP</a>
  <a style="width:108px">EXHIBIT</a>
</nav>

<section class="abs slider">
  <div class="slide" role="img" aria-label="Close-up of a microphone against a warm golden background">
    <h2>TIMELY ANNOUNCEMENTS</h2>
    <div class="dots"><i class="on"></i><i></i><i></i><i></i></div>
  </div>
</section>

<aside class="abs sidebar"></aside>
<div class="bar" style="top:292px"><span class="ico" role="img" aria-label="Sponsors icon"></span>SPONSORS</div>
<div class="abs sponsor-row">
  <span style="width:44px;height:22px;border-radius:3px"></span>
  <span style="width:36px;height:36px;border-radius:50%"></span>
  <span style="width:44px;height:12px;border-radius:2px"></span>
  <span style="width:44px;height:12px;border-radius:2px"></span>
</div>
<div class="cta" style="top:383px">BECOME A SPONSOR <svg width="8" height="12" viewBox="0 0 8 12"><path d="M1.5 1l5 5-5 5" fill="none" stroke="#fff" stroke-width="2"/></svg></div>
<div class="bar" style="top:417px"><span class="ico" role="img" aria-label="Padlock icon"></span>MEMBER LOGIN</div>
<div class="field" style="top:460px">Username</div>
<div class="field" style="top:491px">Password</div>
<div class="abs btn-login">LOGIN</div>
<div class="cta" style="top:559px"><span class="ico" role="img" aria-label="Envelope icon"></span>REGISTER HERE <svg width="8" height="12" viewBox="0 0 8 12"><path d="M1.5 1l5 5-5 5" fill="none" stroke="#fff" stroke-width="2"/></svg></div>
<div class="bar" style="top:592px"><span class="ico" role="img" aria-label="Connected people icon"></span>STAY CONNECTED</div>
<div class="abs social">
  <i style="background:#3b5a9a"></i><i style="background:#2a9fd8"></i><i style="background:#1a77b5"></i><i style="background:#e0452f"></i><i style="background:#f08a22"></i>
</div>

<section class="abs panel welcome">
  <h3>WELCOME</h3>
  <p class="lead">Sed ut perspiciatis unde omnis iste natus error sit voluptatem accusan&shy;tium doloremque laudantium, totam rem aperiam, eaque ipsa quae ab illo inventore veritatis et quasi architecto beatae vitae dicta sunt explicabo.</p>
  <p>Nemo enim ipsam voluptatem quia voluptas sit aspernatur aut odit aut fugit, sed quia consequuntur magni dolores eos qui ratione voluptatem sequi nesciunt. Neque porro quisquam est, qui dolorem ipsum quia dolor sit amet, consectetur, adipisci velit, sed quia non numquam eius modi tempora incidunt ut labore et dolore magnam aliquam quaerat voluptatem</p>
</section>

<section class="abs panel news">
  <h3>LATEST NEWS</h3>
  <article class="news-item">
    <span class="title">How do I use Chirper....</span><span class="date">March 22, 2012</span>
    <p>Do you need to convince your employer of the value ....</p>
    <span class="more">READ MORE</span>
  </article>
  <article class="news-item">
    <span class="title">How do I use Chirper....</span><span class="date">March 22, 2012</span>
    <p>Do you need to convince your employer of the value ....</p>
    <span class="more">READ MORE</span>
  </article>
</section>

<section class="abs panel regions">
  <h3>REGIONS</h3>
  <div class="region-cols">
    <div><h4>MOUNTAIN PACIFIC</h4><ul><li>Vancouver Island</li><li>Vancouver</li><li>Calgary</li></ul></div>
    <div><h4>WESTERN</h4><ul><li>Edmonton</li><li>Saskatchewan</li><li>Winnipeg</li></ul></div>
    <div><h4>CENTRAL</h4><ul><li>National Capital-Ottawa</li><li>Southwestern Ontario</li><li>Montreal</li><li>Toronto</li></ul></div>
    <div><h4>ATLANTIC</h4><ul><li>Nova Scotia</li><li>Terra-Nova, St. John's</li><li>Prince Edward Island</li><li>Atlantic, St. John's</li></ul></div>
  </div>
</section>

<footer class="abs footer">
  <div class="footer-nav">
    <span>Home</span><span class="sep">|</span><span>About</span><span class="sep">|</span><span>Board</span><span class="sep">|</span><span>Chapters</span><span class="sep">|</span><span>Member Space</span><span class="sep">|</span><span>Resources &amp; Knowledge</span><span class="sep">|</span><span>Sponsorship</span><span class="sep">|</span><span>Exhibit</span><span class="sep">|</span><span>Member Login</span><span class="sep">|</span><span>Contact Us</span>
  </div>
  <div class="footer-rule"></div>
  <div class="copyright">© 2013 VELTO Canada Region All rights reserved.</div>
  <div class="privacy">Privacy Policy</div>
</footer>
</body>
</html>
```